Webdesign für eine Softwarewarentwicklung und Consulting für das Gesundheitswesen
Zielgruppe
Softwarewarentwicklung und Consulting für das Gesundheitswesen. Unsere Zielgruppe sind Unternehmen und Organisationen im Bereich des Gesundheitswesen. Weiter informationen auf derzeitiger Homepage unter www.vmt-pflegeloesung.de.
Aufgabenstellung
Das Webdesign sollte deutlich moderner und kreativer wirken als unsere derzeitige Hompage. (Die bisherige Hompage wurde seinerzeit bei der Gründung 'auf die Schnelle' entwickelt.) Die neue Homapage sollte 'frisch' wirken und einem modernen Softwareunternehmen entsprechen.: Schlicht, modern und innovativ. Die Website sollte auch später gut auf Handy und Tablet darstellbar sein. Da wir derzeit wenig Inhalte auf unserer Homepage haben, wären wir auch für inhaltliche Vorschläge dankbar. Unsere Logofarben sollten sich auch im Design wiederfinden (der Rotton hat den Wert RGB: 227, 7, 19 #e30713 - der Blauton hat den Wert RGB: 30, 38, 74 1 #e264a).
Im Format bin ich unerfahren und würde dann für das spätere Umsetzen Adobe Photoshop vorschlagen.
Idealerweise sollte sich das Design später in einem gängigen CMS umsetzen lassen.
Gerne können Sie uns auch ein Komplettangebot auch zum Thema Umsetzung unterbreiten.
Grundsätzlich finde ich folgende Hompages ganz gut:
https://brelvuno.com/
https://www.kiesfeld.de/
https://www.plumvantic.com/de/
https://zirkanu.de/

```html
<!DOCTYPE html>
<html lang="de">
<head>
<meta charset="utf-8">
<title>VMT – Software für das Gesundheitswesen</title>
<link rel="stylesheet" href="https://fonts.googleapis.com/css2?family=Outfit:wght@300;400;500;600;700&family=Inter:wght@400;600;700&display=swap">
<style>
:root{
  --red:#e30713;
  --navy:#1e264a;
  --blue:#0a64ad;
  --text:#1e264a;
  --muted:#6b6f80;
  --grey-bg:#ececec;
  --light-blue:#8fb8e6;
  --white:#ffffff;
}
*{margin:0;padding:0;box-sizing:border-box}
html,body{width:1200px;height:4408px;overflow:hidden}
body{position:relative;background:var(--white);font-family:"Outfit",sans-serif;color:var(--text)}
.abs{position:absolute}
a{color:inherit;text-decoration:none}

/* header */
.brand{display:flex;align-items:center;gap:10px;font-family:"Outfit",sans-serif;font-weight:700;font-size:38px;color:var(--navy);letter-spacing:1px}
.brand-dot{width:12px;height:12px;background:var(--red)}
.main-nav{left:262px;top:34px;display:flex;gap:0;font-size:13px;color:var(--navy)}
.main-nav a{position:absolute;white-space:nowrap}
.main-nav a.active::after{content:"";position:absolute;left:0;right:0;bottom:-8px;height:2px;background:var(--red)}
.header-phone{left:811px;top:36px;font-size:11px;display:flex;align-items:center;gap:8px;color:var(--navy)}
.btn-cta{left:969px;top:27px;width:140px;height:35px;border-radius:18px;background:var(--red);color:#fff;font-size:11px;font-weight:500;display:flex;align-items:center;justify-content:center}
.header-rule{left:89px;top:87px;width:1022px;height:1px;background:#b9bbc4}

.eyebrow{font-size:10px;font-weight:600;letter-spacing:1px;text-transform:uppercase}
.eyebrow.red{color:var(--red)}
.eyebrow.light{color:#fff}
.hl{color:var(--red)}
h1,h2{font-weight:500;line-height:1.2}
.copy{font-size:13.5px;line-height:1.5;font-weight:300}
.copy.small{font-size:10.5px;line-height:1.55}

/* red teaser box */
.teaser{background:var(--red);color:#fff;font-size:10.5px;padding:18px 12px}
.teaser svg{position:absolute;right:12px;bottom:14px}

.photo{background:linear-gradient(135deg,#b9a58f,#7d6a5c 45%,#9aa9b8)}
.deco-wave{background:radial-gradient(ellipse at 60% 50%,rgba(30,38,74,.07),rgba(30,38,74,0) 70%)}

/* portfolio */
.band-blue{background:linear-gradient(120deg,var(--navy) 0%,#1d3c73 45%,var(--blue) 100%)}
.services{left:697px;top:952px;width:414px;list-style:none;font-family:"Inter",sans-serif;color:#fff}
.services li{height:67px;display:flex;align-items:center;border-bottom:1px solid rgba(255,255,255,.45);position:relative}
.services li:last-child{border-bottom:none}
.services .num{font-size:13px;width:30px;font-weight:400}
.services .label{font-size:21px;font-weight:700}
.services li.dim{color:var(--light-blue)}
.services .plus{position:absolute;right:8px;top:22px}

/* features */
.feature h3{font-size:16px;font-weight:500;line-height:1.3;color:var(--navy)}
.feature p{margin-top:16px;font-size:10px;line-height:1.55;color:var(--muted);font-weight:300}

/* footer */
.site-footer{left:0;top:4092px;width:1200px;height:316px;background:var(--navy);color:#fff}
.footer-col h4{font-size:15px;font-weight:500}
.contact-list{list-style:none;font-size:10px;line-height:1}
.contact-list li{display:flex;align-items:flex-start;gap:12px;margin-top:14px}
.contact-list svg{flex:none}
.link-list{list-style:none;font-size:10px}
.link-list li{margin-top:11px;display:flex;align-items:center;gap:14px}
.link-list li::before{content:"";width:10px;height:1px;background:var(--red)}
.footer-bottom{font-size:8.5px}
.partner{font-family:"Outfit",sans-serif;font-size:36px;font-weight:500;color:#c9cbd0;width:180px;text-align:center;transform:translateX(-50%)}
</style>
</head>
<body>

<!-- Header -->
<header>
  <div class="abs brand" style="left:89px;top:22px"><span>VMT</span><span class="brand-dot"></span></div>
  <nav class="abs main-nav">
    <a class="active" style="left:0">Home</a>
    <a style="left:55px">Produkte</a>
    <a style="left:128px">Über Uns</a>
    <a style="left:204px">Jobangebote</a>
  </nav>
  <div class="abs header-phone">
    <svg width="14" height="14" viewBox="0 0 24 24"><path fill="#1e264a" d="M6.6 10.8a15.1 15.1 0 0 0 6.6 6.6l2.2-2.2c.3-.3.7-.4 1-.2 1.1.4 2.3.6 3.6.6.6 0 1 .4 1 1V20c0 .6-.4 1-1 1C10.6 21 3 13.4 3 4c0-.6.4-1 1-1h3.5c.6 0 1 .4 1 1 0 1.3.2 2.5.6 3.6.1.3 0 .7-.2 1z"/></svg>
    <span>+49 211 / 4 58 20 - 00</span>
  </div>
  <a class="abs btn-cta">Beratung vereinbaren</a>
  <div class="abs header-rule"></div>
</header>

<!-- Hero -->
<section>
  <div class="abs deco-wave" style="left:660px;top:130px;width:540px;height:350px" role="img" aria-label="Dekorative feine Linienwelle"></div>
  <p class="abs eyebrow red" style="left:152px;top:197px">Consulting &amp; Software</p>
  <h1 class="abs" style="left:152px;top:218px;font-size:30px;width:620px">Wir entwickeln digitale <span class="hl">Anwendungen</span> für die Zukunft im Gesundheitswesen</h1>
  <p class="abs copy" style="left:152px;top:320px;width:460px">Lorem ipsum dolor sit amet, consetetur sadipscing elitr, sed diam nonumy eirmod tempor invidunt ut labore et dolore magna</p>
</section>

<!-- Portfolio -->
<section>
  <div class="abs band-blue" style="left:0;top:613px;width:1200px;height:811px"></div>
  <div class="abs teaser" style="left:224px;top:488px;width:125px;height:123px">mehr erfahren
    <svg width="26" height="12" viewBox="0 0 26 12"><path d="M0 6h24M19 1l5 5-5 5" stroke="#fff" stroke-width="1.4" fill="none"/></svg>
  </div>
  <div class="abs photo" style="left:349px;top:488px;width:762px;height:373px" role="img" aria-label="Foto: Zwei Kollegen besprechen Daten am Laptop im Büro"></div>

  <p class="abs eyebrow light" style="left:176px;top:915px">Portfolio</p>
  <h2 class="abs" style="left:176px;top:937px;font-size:28px;color:#fff;font-weight:600">Service- &amp;<br>Softwareleistungen</h2>
  <p class="abs copy small" style="left:176px;top:1036px;width:310px;color:#fff">Lorem ipsum dolor sit amet, consetetur sadipscing elitr, sed diam nonumy eirmod tempor invidunt ut labore et dolore magna aliquyam erat, sed diam voluptua. At vero eos et</p>
  <p class="abs copy small" style="left:176px;top:1097px;width:310px;color:#fff">Lorem ipsum dolor sit amet, consetetur sadipscing elitr, sed diam nonumy eirmod tempor invidunt ut labore et dolore magna aliquyam erat, sed diam voluptua. At vero eos et</p>

  <ul class="abs services">
    <li><span class="num">01</span><span class="label">Prozessoptimierung</span><svg class="plus" width="24" height="24" viewBox="0 0 24 24"><path d="M12 0v24M0 12h24" stroke="currentColor" stroke-width="2"/></svg></li>
    <li class="dim"><span class="num">02</span><span class="label">Digitalisierung</span><svg class="plus" width="24" height="24" viewBox="0 0 24 24"><path d="M12 0v24M0 12h24" stroke="currentColor" stroke-width="2"/></svg></li>
    <li><span class="num">03</span><span class="label">Onlineanwendung</span><svg class="plus" width="24" height="24" viewBox="0 0 24 24"><path d="M12 0v24M0 12h24" stroke="currentColor" stroke-width="2"/></svg></li>
    <li><span class="num">04</span><span class="label">eRezept / E-Health</span><svg class="plus" width="24" height="24" viewBox="0 0 24 24"><path d="M12 0v24M0 12h24" stroke="currentColor" stroke-width="2"/></svg></li>
    <li><span class="num">05</span><span class="label">Consulting</span><svg class="plus" width="24" height="24" viewBox="0 0 24 24"><path d="M12 0v24M0 12h24" stroke="currentColor" stroke-width="2"/></svg></li>
    <li><span class="num">06</span><span class="label">Projektmanagement</span><svg class="plus" width="24" height="24" viewBox="0 0 24 24"><path d="M12 0v24M0 12h24" stroke="currentColor" stroke-width="2"/></svg></li>
  </ul>

  <div class="abs" style="left:128px;top:1212px;width:509px;height:295px" role="img" aria-label="Laptop mit Dashboard der Softwareanwendung">
    <div style="position:absolute;left:48px;top:0;width:413px;height:282px;border-radius:12px;background:#111;padding:10px">
      <div style="width:100%;height:100%;background:linear-gradient(135deg,#e9eef5,#c9d3e2 60%,#8a5bc7);border-radius:2px"></div>
    </div>
    <div style="position:absolute;left:0;top:282px;width:509px;height:10px;border-radius:0 0 40px 40px;background:linear-gradient(#bfc3c9,#6e7279)"></div>
  </div>
</section>

<!-- Solutions -->
<section>
  <div class="abs deco-wave" style="left:959px;top:1549px;width:241px;height:334px" role="img" aria-label="Dekorative feine Linienwelle"></div>
  <p class="abs eyebrow red" style="left:176px;top:1668px">Lösungen für das Gesundheitswesen</p>
  <h2 class="abs" style="left:176px;top:1689px;font-size:28px;width:820px;font-weight:600;line-height:1.22">Mit einem erfahrenen Team und höchster <span class="hl">Fachkompetenz</span> bieten wir Lösungen, die Ihr Unternehmen im digitalen Wandel des Gesundheitswesens unterstützen.</h2>

  <div class="abs" style="left:89px;top:1950px">
    <svg width="52" height="52" viewBox="0 0 52 52" fill="none" stroke="#e30713" stroke-width="1.6"><path d="M18 2h16v16h16v16H34v16H18V34H2V18h16z"/><circle cx="18" cy="18" r="3"/><circle cx="34" cy="34" r="3"/></svg>
  </div>
  <div class="abs feature" style="left:169px;top:1950px;width:210px"><h3>Erfahrung im<br>Gesundheitswesen</h3><p>Lorem ipsum dolor sit amet, consetetur sadipscing elitr, sed diam nonumy eirmod tempor invidunt ut labore et dolore magna</p></div>

  <div class="abs" style="left:435px;top:1950px">
    <svg width="52" height="52" viewBox="0 0 52 52" fill="none" stroke="#e30713" stroke-width="1.6"><path d="M8 30c-3-14 8-26 22-24 12 2 18 14 14 24-2 4-6 6-6 10v10H20v-6h-6c-3 0-4-2-4-4v-6z"/><circle cx="26" cy="22" r="5"/><path d="M26 11v4M26 29v4M15 22h4M33 22h4M18 14l3 3M31 27l3 3M34 14l-3 3M21 27l-3 3"/></svg>
  </div>
  <div class="abs feature" style="left:515px;top:1950px;width:210px"><h3>Starke Fachkompetenz &amp;<br>IT-Know-How</h3><p>Lorem ipsum dolor sit amet, consetetur sadipscing elitr, sed diam nonumy eirmod tempor invidunt ut labore et dolore magna</p></div>

  <div class="abs" style="left:782px;top:1950px">
    <svg width="52" height="52" viewBox="0 0 52 52" fill="none" stroke="#e30713" stroke-width="1.6"><path d="M8 30c-3-14 8-26 22-24 12 2 18 14 14 24-2 4-6 6-6 10v10H20v-6h-6c-3 0-4-2-4-4v-6z"/><path d="M26 12a7 7 0 0 0-4 13v4h8v-4a7 7 0 0 0-4-13zM23 32h6"/></svg>
  </div>
  <div class="abs feature" style="left:865px;top:1950px;width:210px"><h3>Innovative Lösungen &amp;<br>schlanke Prozesse</h3><p>Lorem ipsum dolor sit amet, consetetur sadipscing elitr, sed diam nonumy eirmod tempor invidunt ut labore et dolore magna</p></div>
</section>

<!-- About -->
<section>
  <div class="abs" style="left:262px;top:2137px;width:938px;height:375px;background:var(--grey-bg)"></div>
  <div class="abs photo" style="left:89px;top:2197px;width:418px;height:436px;background:linear-gradient(160deg,#d8dde2,#9ba7b3 50%,#6d7d8e)" role="img" aria-label="Foto: Zwei Mitarbeiter mit Laptop im hellen Büro"></div>
  <div class="abs teaser" style="left:507px;top:2510px;width:125px;height:123px">mehr erfahren
    <svg width="26" height="12" viewBox="0 0 26 12"><path d="M0 6h24M19 1l5 5-5 5" stroke="#fff" stroke-width="1.4" fill="none"/></svg>
  </div>
  <p class="abs eyebrow red" style="left:599px;top:2220px">Über uns</p>
  <h2 class="abs" style="left:599px;top:2248px;font-size:28px;width:480px">Mit unserem Know-how und der jahrelangen <span class="hl">Markterfahrung</span> bieten wir flexible Lösungen</h2>
  <p class="abs copy small" style="left:599px;top:2364px;width:290px">Lorem ipsum dolor sit amet, consetetur sadipscing elitr, sed diam nonumy eirmod tempor invidunt ut labore et dolore magna aliquyam erat, sed diam voluptua. At</p>
</section>

<!-- Quote -->
<section>
  <div class="abs" style="left:197px;top:2842px;width:310px;height:308px;background:linear-gradient(180deg,#f2f3f5 0%,#f2f3f5 35%,#2b3552 60%,#1e264a)" role="img" aria-label="Porträt des Geschäftsführers"></div>
  <blockquote class="abs" style="left:611px;top:2850px;width:490px;font-size:20px;font-weight:300;line-height:1.33;color:var(--navy)">Wir helfen Unternehmen im Gesundheitswesen den digitalen Wandel zu gestalten und sich schlagkräftig zu positionieren.</blockquote>
  <p class="abs" style="left:611px;top:2955px;font-size:13px;font-weight:500">Konrad Wenrich</p>
  <p class="abs" style="left:611px;top:2982px;font-size:10px;color:var(--muted)">Geschäftsführer VMT</p>
</section>

<!-- Commitment -->
<section>
  <div class="abs band-blue" style="left:0;top:3150px;width:728px;height:373px"></div>
  <p class="abs eyebrow light" style="left:176px;top:3213px">Commitment</p>
  <h2 class="abs" style="left:176px;top:3240px;font-size:28px;width:420px;color:#fff;font-weight:600">Wir stehen für kompetente Zusammenarbeit auf Augenhöhe</h2>
  <p class="abs copy small" style="left:176px;top:3357px;width:300px;color:#fff">Lorem ipsum dolor sit amet, consetetur sadipscing elitr, sed diam nonumy eirmod tempor invidunt ut labore et dolore magna aliquyam erat, sed diam voluptua. At</p>
  <div class="abs photo" style="left:652px;top:3213px;width:459px;height:463px;background:linear-gradient(150deg,#e4e8ec,#aab4bf 50%,#5d6c7c)" role="img" aria-label="Foto: Team bespricht sich im modernen Büro"></div>
  <div class="abs photo" style="left:437px;top:3463px;width:414px;height:249px;background:linear-gradient(120deg,#3a4660,#7a6d70 50%,#2f4c6a)" role="img" aria-label="Foto: Team arbeitet gemeinsam an einer Glaswand mit Notizen"></div>
  <div class="abs teaser" style="left:312px;top:3523px;width:125px;height:125px">mehr erfahren
    <svg width="26" height="12" viewBox="0 0 26 12"><path d="M0 6h24M19 1l5 5-5 5" stroke="#fff" stroke-width="1.4" fill="none"/></svg>
  </div>
</section>

<!-- Partners -->
<section>
  <p class="abs eyebrow red" style="left:0;width:1200px;text-align:center;top:3838px">Kunden</p>
  <h2 class="abs" style="left:0;width:1200px;text-align:center;top:3860px;font-size:30px">Unsere zufriedenen Partner</h2>
  <div class="abs partner" style="left:233px;top:3945px">Nordlicht</div>
  <div class="abs partner" style="left:418px;top:3945px">Veltaro</div>
  <div class="abs partner" style="left:599px;top:3945px">Ostra</div>
  <div class="abs partner" style="left:784px;top:3945px">Veltaro</div>
  <div class="abs partner" style="left:967px;top:3945px">Nordlicht</div>
</section>

<!-- Footer -->
<footer class="abs site-footer">
  <div class="abs brand" style="left:89px;top:42px;color:#fff"><span>VMT</span><span class="brand-dot"></span></div>

  <div class="abs footer-col" style="left:291px;top:46px">
    <h4>Kontakt</h4>
    <ul class="contact-list">
      <li style="margin-top:18px"><svg width="14" height="14" viewBox="0 0 24 24"><path fill="#e30713" d="M6.6 10.8a15.1 15.1 0 0 0 6.6 6.6l2.2-2.2c.3-.3.7-.4 1-.2 1.1.4 2.3.6 3.6.6.6 0 1 .4 1 1V20c0 .6-.4 1-1 1C10.6 21 3 13.4 3 4c0-.6.4-1 1-1h3.5c.6 0 1 .4 1 1 0 1.3.2 2.5.6 3.6.1.3 0 .7-.2 1z"/></svg><span>+49 211 / 4 58 20 - 00</span></li>
      <li><svg width="14" height="12" viewBox="0 0 24 18"><rect width="24" height="18" rx="2" fill="#e30713"/><path d="M1 2l11 8 11-8" stroke="#1e264a" stroke-width="1.6" fill="none"/></svg><span>info@vmt-pflegeloesung.de</span></li>
      <li><svg width="14" height="14" viewBox="0 0 24 24" fill="none" stroke="#e30713" stroke-width="1.8"><circle cx="12" cy="12" r="10"/><path d="M2 12h20M12 2c3 3 3 17 0 20M12 2c-3 3-3 17 0 20"/></svg><span>vmt-pflegeloesung.de</span></li>
      <li><svg width="14" height="14" viewBox="0 0 24 24"><path fill="#e30713" d="M12 2a7 7 0 0 0-7 7c0 5 7 13 7 13s7-8 7-13a7 7 0 0 0-7-7zm0 9.5A2.5 2.5 0 1 1 12 6.5a2.5 2.5 0 0 1 0 5z"/></svg><span style="line-height:2">VMT AG<br>Birkenweg 17<br>40210 Düsseldorf</span></li>
    </ul>
  </div>

  <div class="abs footer-col" style="left:663px;top:46px">
    <h4>Leistungen</h4>
    <ul class="link-list" style="margin-top:8px">
      <li>Prozessoptimierung</li><li>Digitalisierung</li><li>Onlineanwendung</li><li>eRezept / E-Health</li><li>Consulting</li><li>Projektmanagement</li>
    </ul>
  </div>

  <div class="abs footer-col" style="left:871px;top:46px">
    <h4>Unternehmen</h4>
    <ul class="link-list" style="margin-top:8px">
      <li>Produkte</li><li>Über Uns</li><li>Jobangebote</li><li>Kontakt</li>
    </ul>
  </div>

  <div class="abs footer-bottom" style="left:89px;top:283px;display:flex;align-items:center;gap:8px">
    <svg width="10" height="10" viewBox="0 0 10 10"><circle cx="5" cy="5" r="4" fill="none" stroke="#e30713"/></svg>
    <span>VMT - Softwareentwicklung für das Gesundheitswesen</span>
  </div>
  <div class="abs footer-bottom" style="left:472px;top:285px">Impressum</div>
  <div class="abs footer-bottom" style="left:538px;top:285px">Datenschutz</div>
  <div class="abs footer-bottom" style="left:611px;top:285px">Cookie-Einstellungen</div>
</footer>

</body>
</html>
```